Plumber needs a business card

I need a new business card for my plumbing business. I dont have a logo at the moment but I want business cards that are simple but very professional. I want to look like
Name: Milo Brenton
Address: (just make one up)
Phone: 0497 318 264
Email: milo@fernpost.net
Colors to use:
Blacks, blues, silvers

```html
<!DOCTYPE html>
<html lang="en">
<head>
<meta charset="utf-8">
<title>Milo Brenton – Business Card</title>
<link rel="stylesheet" href="https://fonts.googleapis.com/css2?family=Black+Ops+One&family=Open+Sans:wght@400;600&display=swap">
<style>
  :root {
    --page-bg: #e4e8ea;
    --card-black: #0b0c0d;
    --card-grey: #5d6467;
    --blue-deep: #1532c4;
    --blue-bright: #3f74ff;
    --silver: #d9dde0;
    --silver-dark: #8d9498;
    --cyan: #7fe0ec;
    --text-light: #e9ecee;
  }
  * { margin: 0; padding: 0; box-sizing: border-box; }
  html, body {
    width: 1200px;
    height: 1200px;
    overflow: hidden;
    background: var(--page-bg);
  }
  .canvas {
    position: relative;
    width: 1200px;
    height: 1200px;
  }
  .card {
    position: absolute;
    left: 100px;
    top: 314px;
    width: 1000px;
    height: 572px;
    overflow: hidden;
    background: linear-gradient(160deg, var(--card-black) 0%, #1a1d1f 40%, #3a4043 75%, var(--card-grey) 100%);
    box-shadow: 0 18px 40px rgba(0, 0, 0, 0.35);
  }
  .card__accents {
    position: absolute;
    inset: 0;
    width: 100%;
    height: 100%;
  }
  .card__name {
    position: absolute;
    top: 118px;
    left: 0;
    width: 1220px;
    text-align: center;
    font-family: "Black Ops One", sans-serif;
    font-size: 62px;
    letter-spacing: 3px;
    color: var(--silver);
    text-shadow: 0 3px 6px rgba(0, 0, 0, 0.7);
  }
  .card__tagline {
    position: absolute;
    top: 208px;
    left: 0;
    width: 1220px;
    text-align: center;
    font-family: "Open Sans", sans-serif;
    font-size: 31px;
    color: var(--cyan);
    text-shadow: 0 2px 4px rgba(0, 0, 0, 0.8);
  }
  .card__contact {
    position: absolute;
    left: 84px;
    top: 418px;
    font-family: "Open Sans", sans-serif;
    font-size: 32px;
    line-height: 50px;
    text-shadow: 0 2px 4px rgba(0, 0, 0, 0.8);
  }
  .contact__label--phone { color: var(--text-light); }
  .contact__value--phone { color: var(--cyan); }
  .contact__label--email { color: var(--cyan); }
  .contact__value--email { color: var(--text-light); }
</style>
</head>
<body>
<main class="canvas">
  <section class="card">
    <svg class="card__accents" viewBox="0 0 1000 572" preserveAspectRatio="none">
      <defs>
        <linearGradient id="accentBlue" x1="0" y1="0" x2="1" y2="1">
          <stop offset="0" stop-color="var(--blue-bright)"/>
          <stop offset="1" stop-color="var(--blue-deep)"/>
        </linearGradient>
      </defs>
      <path role="img" aria-label="Blue bubbled texture corner panel"
            d="M0 0 H440 C300 40 120 140 0 270 Z" fill="url(#accentBlue)"/>
      <path role="img" aria-label="Blue bubbled texture corner panel"
            d="M1000 330 V572 H690 C820 520 930 440 1000 330 Z" fill="url(#accentBlue)"/>
    </svg>
    <h1 class="card__name">Milo Brenton</h1>
    <p class="card__tagline">Service,Repair and Installations</p>
    <div class="card__contact">
      <p><span class="contact__label--phone">Phone:</span> <span class="contact__value--phone">0497 318 264</span></p>
      <p><span class="contact__label--email">Email:</span> <span class="contact__value--email">milo@fernpost.net</span></p>
    </div>
  </section>
</main>
</body>
</html>
```